Motivationskarten für Trainer und Coach
Zielgruppe
Ich bin Trainer und Coach mit Schwerpunkt Effizienz/ Zeit- und Selbstmanagement sowie Büroorganisation. Meine Kunden buchen bei mir Seminare, um Ihren Arbeitsalltag effizienter zu gestalten und zu strukturieren und Ihre Büroabläufe sowie Prozesse zu optimieren.
Ich möchte gerne 3 verschiedene Postkarten mit Sprüchen von mir gestalten. Postkarten, die man auch verschicken kann und aus denen natürlich meine Kontaktdaten hervorgehen. Mein Logo sollte irgendwo auf der beschreibbaren Seite sichtbar sein. Vorne drauf nur der Spruch und vielleicht eine Zeichnung, eine Karikatur, eine Comiczeichnung oder ein Bild (ich bin offen für alles).
Die Sprüche lauten:
Lieber unperfekt anfangen als gar nicht!
Mach Dir hin und wieder bewusst, wie großartig Du bist!
Frage Dich immer: 'Was ist das Schlimmste, was passieren könnte?' - Es ist selten ein Weltuntergang.
Es sollen drei verschiedene Karten sein, die aber irgendwie zusammenpassen vom Design her.
Meine Hauptzielgruppe, für die auch diese Postkarten hier gedacht sind, sind vor allem Frauen - entweder Frauen, die als Assistentin arbeiten oder selbständig sind.
Aufgabenstellung
Es darf gerne etwas weiblich sein, sollte aber nicht zu bunt und schnörkelig sein. Es darf gerne auffallen. Achtung: Mein Logo sollte ohne Untertitel verwendet werden. Also nur 'Wiebke Harlach' - ohne 'Training & Coaching'.

```html
<!DOCTYPE html>
<html lang="de">
<head>
<meta charset="utf-8">
<title>Wiebke Harlach – Postkarte</title>
<link href="https://fonts.googleapis.com/css2?family=Jura:wght@500&family=Roboto+Condensed:wght@300;400;700&display=swap" rel="stylesheet">
<style>
  :root {
    --bg: #e4e4e4;
    --card: #ffffff;
    --ink: #2f3236;
    --slate: #4a4e55;
    --green: #5c9c1e;
    --green-dark: #2f7d1a;
    --green-light: #7cb526;
    --rule: #7a7d82;
    --photo-a: #c9b28e;
    --photo-b: #e6c6ae;
    --photo-c: #8f7a5c;
  }
  html, body {
    margin: 0;
    width: 1200px;
    height: 1200px;
    overflow: hidden;
    background: var(--bg);
  }
  .stage {
    position: relative;
    width: 1200px;
    height: 1200px;
  }
  .card-back {
    position: absolute;
    left: 101px;
    top: 568px;
    width: 825px;
    height: 546px;
    background: var(--card);
    font-family: "Roboto Condensed", "Arial Narrow", sans-serif;
    color: var(--ink);
  }
  .brand {
    position: absolute;
    left: 40px;
    top: 58px;
    display: flex;
    align-items: center;
    gap: 10px;
    font-family: "Roboto Condensed", sans-serif;
    font-weight: 700;
    font-size: 19px;
    letter-spacing: 0.5px;
    color: var(--slate);
    text-transform: uppercase;
  }
  .brand-dot {
    width: 16px;
    height: 16px;
    border-radius: 50%;
    background: var(--green);
  }
  .intro {
    position: absolute;
    left: 40px;
    top: 142px;
    width: 290px;
    margin: 0;
    font-weight: 300;
    font-size: 13.4px;
    line-height: 19px;
  }
  .contact {
    position: absolute;
    left: 40px;
    top: 238px;
    margin: 0;
    font-weight: 300;
    font-size: 13.4px;
    line-height: 19px;
  }
  .divider {
    position: absolute;
    left: 415px;
    top: 156px;
    width: 5px;
    height: 358px;
    background: var(--slate);
  }
  .address-line {
    position: absolute;
    left: 457px;
    width: 348px;
    height: 1px;
    background: var(--rule);
  }
  .card-front {
    position: absolute;
    left: 546px;
    top: 107px;
    width: 553px;
    height: 773px;
    overflow: hidden;
  }
  .photo {
    position: absolute;
    inset: 0;
    background:
      radial-gradient(ellipse 45% 40% at 58% 40%, var(--photo-b), transparent 75%),
      linear-gradient(100deg, var(--photo-c) 0%, var(--photo-a) 35%, var(--photo-b) 60%, var(--photo-a) 100%);
  }
  .front-shapes {
    position: absolute;
    inset: 0;
  }
  .quote {
    position: absolute;
    left: 38px;
    top: 572px;
    margin: 0;
    font-family: "Jura", "Eurostile", sans-serif;
    font-weight: 500;
    font-size: 38px;
    line-height: 42px;
    color: #ffffff;
  }
</style>
</head>
<body>
<div class="stage">
  <section class="card-back">
    <div class="brand"><span class="brand-dot"></span>Wiebke Harlach</div>
    <p class="intro">Ich biete Ihnen Trainings und Coachings mit Schwer­punkt Effizienz/Zeit- und Selbstmanagement sowie Büroorganisation um Ihren Arbeitsalltag effizienter zu gestalten und zu strukturieren.</p>
    <p class="contact">Kontakt unter<br>Tel.: 0177/98765432<br>E-Mail: info@wiebke-harlach.de</p>
    <div class="divider"></div>
    <div class="address-line" style="top:350px"></div>
    <div class="address-line" style="top:409px"></div>
    <div class="address-line" style="top:470px"></div>
  </section>

  <section class="card-front">
    <div class="photo" role="img" aria-label="Foto einer blonden Frau, die frech die Zunge herausstreckt und ein Auge zukneift"></div>
    <svg class="front-shapes" viewBox="0 0 553 773" preserveAspectRatio="none" aria-hidden="true">
      <path d="M0 277 C90 470 300 610 553 625 L553 773 L0 773 Z" fill="#4f9a1c" opacity="0.85"/>
      <path d="M0 357 C120 500 330 560 553 560 L553 773 L0 773 Z" fill="#7cb526" opacity="0.45"/>
      <path d="M0 520 C150 640 350 700 553 680 L553 773 L0 773 Z" fill="#2f7d1a" opacity="0.55"/>
    </svg>
    <p class="quote">Mach Dir hin und<br>wieder bewusst, wie<br>großartig Du bist!</p>
  </section>
</div>
</body>
</html>
```